Tavolin brise

i am a designer who works with home-based business. i want to give surprise to my sister with describing a luxurious display at her blog.
two days later she would be birthday

Business

```html
<!DOCTYPE html>
<html lang="en">
<head>
<meta charset="utf-8">
<title>This Is Tavolin Brise</title>
<link rel="stylesheet" href="https://fonts.googleapis.com/css2?family=Ubuntu:wght@400;500;700&family=PT+Sans:wght@400;700&display=swap">
<style>
  :root {
    --page-bg: #2f4553;
    --title-white: #f4f4f4;
    --title-yellow: #f7e21b;
    --nav-top: #45b2ee;
    --nav-bottom: #1f86cd;
    --heading-grey: #6e6e6e;
    --text-grey: #6a6a6a;
    --title-dark: #3e3e3e;
    --link-blue: #1f5fae;
    --comment-blue: #3c6c9c;
    --copyright-blue: #47698e;
    --input-top: #a9a9a9;
    --input-bottom: #8c8c8c;
    --rule: #cfcfcf;
    --panel-edge: #c4c4c4;
    --frame: #ffffff;
    --swoosh-top: #3ea6e6;
    --swoosh-bottom: #1a70b8;
    --rss-orange: #f0771c;
  }
  * { box-sizing: border-box; margin: 0; padding: 0; }
  html, body { width: 1200px; height: 974px; overflow: hidden; }
  body {
    position: relative;
    background: var(--page-bg);
    font-family: "PT Sans", sans-serif;
    color: var(--text-grey);
  }

  .site-title {
    position: absolute; left: 32px; top: 34px;
    font-family: "Ubuntu", sans-serif; font-weight: 700; font-size: 32px;
    color: var(--title-white); letter-spacing: -0.3px;
  }
  .site-title .name { color: var(--title-yellow); }

  .frame-wrap { position: absolute; left: 33px; top: 91px; width: 1137px; height: 854px; overflow: hidden; }

  .nav {
    position: absolute; left: 0; top: 0; width: 1137px; height: 57px;
    background: linear-gradient(var(--nav-top), var(--nav-bottom));
  }
  .nav a {
    position: absolute; top: 18px; color: #fff; text-decoration: none;
    font-family: "Ubuntu", sans-serif; font-size: 16px; font-weight: 500;
  }
  .rss { position: absolute; left: 929px; top: 12px; }
  .search {
    position: absolute; left: 957px; top: 13px; width: 164px; height: 30px;
    background: #fff; border-radius: 6px; font-size: 14px; color: #777;
    padding: 6px 0 0 12px;
  }
  .search svg { position: absolute; right: 9px; top: 8px; }

  .hero-panel {
    position: absolute; left: 0; top: 57px; width: 660px; height: 433px;
    background: linear-gradient(#fafafa, #ececec 60%, #e2e2e2);
    border-right: 3px solid var(--panel-edge);
  }
  .stories-panel {
    position: absolute; left: 663px; top: 57px; width: 474px; height: 433px;
    background: linear-gradient(#efefef, #e4e4e4 70%, #d9d9d9);
  }
  .slide-frame {
    position: absolute; left: 26px; top: 25px; width: 588px; height: 370px;
    background: var(--frame); box-shadow: 0 2px 6px rgba(0,0,0,.25);
  }
  .slide-photo {
    position: absolute; left: 13px; top: 13px; width: 561px; height: 343px;
    background: radial-gradient(ellipse at 55% 40%, #6f7c6a, #35483f 45%, #1a2420 85%);
    overflow: hidden;
  }
  .slide-caption {
    position: absolute; left: 0; bottom: 0; width: 100%; height: 55px;
    background: rgba(20,24,22,.55); color: #fff; padding: 8px 0 0 17px;
    font-size: 13.5px; line-height: 18px;
  }
  .slide-caption b { font-size: 14px; }
  .slide-tab {
    position: absolute; left: -3px; top: 156px; width: 36px; height: 70px;
    background: linear-gradient(90deg, #f5f5f5, #dcdcdc); border-radius: 0 6px 6px 0;
    box-shadow: 1px 1px 4px rgba(0,0,0,.3);
  }
  .slide-tab svg { position: absolute; left: 9px; top: 22px; }

  .heading {
    position: absolute; font-family: "Ubuntu", sans-serif; font-weight: 500;
    font-size: 23px; color: var(--heading-grey);
  }
  .thumb-frame {
    position: absolute; width: 179px; height: 139px; background: var(--frame);
    box-shadow: 0 1px 5px rgba(0,0,0,.25);
  }
  .thumb-frame .pic { position: absolute; left: 9px; top: 9px; width: 161px; height: 121px; }
  .pic-meadow { background: radial-gradient(circle at 55% 40%, #e6e27a, #7fae2e 40%, #3f6b14 90%); }
  .pic-parchment { background: linear-gradient(120deg, #c9a570, #e3cda0 45%, #b58a52); }

  .story { position: absolute; width: 236px; font-size: 13.5px; line-height: 16.6px; }
  .story b { display: block; color: var(--title-dark); font-size: 14px; }
  .story a, .item a { color: var(--link-blue); text-decoration: none; }

  .bottom-area {
    position: absolute; left: 0; top: 490px; width: 1137px; height: 364px;
    background: linear-gradient(#f4f4f4, #e9e9e9 70%, #dcdcdc);
  }
  .swoosh { position: absolute; left: 868px; top: 490px; }
  .comments-title {
    position: absolute; right: 10px; top: 504px; color: #fff;
    font-family: "Ubuntu", sans-serif; font-weight: 500; font-size: 19px;
  }
  .divider { position: absolute; top: 513px; width: 1px; height: 305px; background: var(--rule); }
  .rule { position: absolute; height: 1px; background: var(--rule); }

  .mini { position: absolute; width: 62px; height: 52px; }
  .item { position: absolute; font-size: 13.5px; line-height: 16.6px; width: 170px; }
  .item b { display: block; color: var(--title-dark); font-size: 14px; }

  .copyright {
    position: absolute; left: 25px; top: 788px; color: var(--copyright-blue);
    font-family: "Ubuntu", sans-serif; font-weight: 500; font-size: 20px; line-height: 24px;
  }

  .field {
    position: absolute; left: 300px; width: 171px; color: #f4f4f4; font-size: 13.5px;
    background: linear-gradient(var(--input-top), var(--input-bottom));
    padding: 6px 0 0 10px;
  }
  .submit {
    position: absolute; left: 300px; top: 760px; width: 85px; height: 29px;
    background: linear-gradient(#9a9a9a, #6f6f6f); color: #fff; font-weight: 700;
    font-size: 14px; text-align: center; padding-top: 5px;
  }

  .social { position: absolute; font-family: "Ubuntu", sans-serif; font-weight: 700; color: #7a7a7a; }
  .social-dot { position: absolute; border-radius: 50%; background: #8fcbeb; }
  .social-square { position: absolute; border-radius: 8px; background: #4f6ea8; }

  .comment { position: absolute; left: 904px; font-size: 13.5px; line-height: 16.6px; width: 180px; }
  .comment b { display: block; color: var(--comment-blue); font-size: 14px; }
  .comment-thumb {
    position: absolute; left: 817px; width: 68px; height: 56px; background: #fff;
    box-shadow: 0 1px 4px rgba(0,0,0,.3);
  }
  .comment-thumb .pic { position: absolute; left: 4px; top: 4px; width: 60px; height: 48px; }
</style>
</head>
<body>
  <div class="site-title">This Is <span class="name">Tavolin Brise</span></div>

  <div class="frame-wrap">
    <nav class="nav">
      <a style="left:30px">Home</a>
      <a style="left:100px">My Profile</a>
      <a style="left:202px">My Stories</a>
      <a style="left:309px">Contact</a>
      <a style="left:396px">Gallery</a>
      <a style="left:467px">Downloads</a>
      <a style="left:568px">Other Menu</a>
      <svg class="rss" width="32" height="32" viewBox="0 0 32 32" aria-label="Feed">
        <rect x="1" y="1" width="30" height="30" rx="7" fill="var(--rss-orange)"/>
        <circle cx="9" cy="23" r="3" fill="#fff"/>
        <path d="M7 14a11 11 0 0 1 11 11" stroke="#fff" stroke-width="3.5" fill="none"/>
        <path d="M7 7a18 18 0 0 1 18 18" stroke="#fff" stroke-width="3.5" fill="none"/>
      </svg>
      <div class="search">Search...
        <svg width="16" height="14" viewBox="0 0 16 14"><circle cx="6" cy="6" r="4.5" stroke="#aaa" stroke-width="2" fill="none"/><path d="M9.5 9 14 13" stroke="#aaa" stroke-width="2.4"/></svg>
      </div>
    </nav>

    <section class="hero-panel">
      <div class="slide-frame">
        <div class="slide-photo" role="img" aria-label="Fairy-tale scene of a girl kneeling among giant mushrooms under a cloudy night sky">
          <div class="slide-caption"><b>This is tavolin brise</b><br>Your Text Description of photo in here : )</div>
        </div>
      </div>
      <div class="slide-tab">
        <svg width="18" height="26" viewBox="0 0 18 26"><path d="M4 3l10 10L4 23" stroke="#9a9a9a" stroke-width="4" fill="none"/></svg>
      </div>
    </section>

    <section class="stories-panel">
      <div class="heading" style="left:27px;top:20px">Lastest Stories</div>
      <div class="thumb-frame" style="left:24px;top:68px"><div class="pic pic-meadow" role="img" aria-label="Glowing tree on a green meadow"></div></div>
      <div class="story" style="left:221px;top:69px"><b>This is tavolin brise</b>Your short stories in here.. Your short stories in here.Your short stories in here Your short stories in here..Your short stories in here.. Your short stories in here...<br><a style="display:block;margin-top:4px">Read More</a></div>
      <div class="thumb-frame" style="left:24px;top:232px"><div class="pic pic-parchment" role="img" aria-label="Colourful road lines on aged paper"></div></div>
      <div class="story" style="left:221px;top:238px"><b>Your Title Story</b>Your short stories in here.. Your short stories in here.Your short stories in here Your short stories in here..<br><a style="display:block;margin-top:8px">Read More</a></div>
    </section>

    <section class="bottom-area"></section>
    <svg class="swoosh" width="269" height="135" viewBox="0 0 269 135">
      <defs><linearGradient id="swooshFill" x1="0" y1="0" x2="0" y2="1"><stop offset="0" stop-color="var(--swoosh-top)"/><stop offset="1" stop-color="var(--swoosh-bottom)"/></linearGradient></defs>
      <path d="M0 0H269V135C240 95 215 75 175 62C120 44 50 42 0 0Z" fill="url(#swooshFill)"/>
    </svg>
    <div class="comments-title">Tavolin Brise Comments</div>

    <div class="divider" style="left:276px"></div>
    <div class="divider" style="left:500px"></div>
    <div class="divider" style="left:792px"></div>

    <div class="heading" style="left:25px;top:515px">Bottom Menu</div>
    <div class="mini pic-parchment" style="left:25px;top:558px" role="img" aria-label="Colourful road lines on aged paper"></div>
    <div class="item" style="left:95px;top:553px"><b>Your Title Story</b>Your short stories in here..<br>Your short stories in here.<br><a>Read More</a></div>
    <div class="rule" style="left:25px;top:636px;width:159px"></div>
    <div class="mini pic-parchment" style="left:25px;top:655px" role="img" aria-label="Colourful road lines on aged paper"></div>
    <div class="item" style="left:95px;top:651px"><b>Your Title Story</b>Your short stories in here..<br>Your short stories in here.<br><a>Read More</a></div>
    <div class="rule" style="left:25px;top:739px;width:159px"></div>
    <div class="copyright">Copyright<br>Your Website</div>

    <div class="heading" style="left:300px;top:516px">Contact Me</div>
    <div class="field" style="top:562px;height:29px">Your Name</div>
    <div class="field" style="top:604px;height:29px">Your Email</div>
    <div class="field" style="top:647px;height:99px">Your Message</div>
    <div class="submit">Submit</div>

    <div class="heading" style="left:520px;top:516px">Social Network</div>
    <div class="social-dot" style="left:545px;top:578px;width:46px;height:46px"></div>
    <div class="social" style="left:602px;top:586px;font-size:20px;line-height:22px">Follow Me<br>On Chirper</div>
    <div class="social-square" style="left:537px;top:680px;width:74px;height:76px"></div>
    <div class="social" style="left:621px;top:690px;font-size:21px;line-height:25px">Find Me<br>On Pagebook</div>

    <div class="comment-thumb" style="top:558px"><div class="pic pic-parchment" role="img" aria-label="Colourful road lines on aged paper"></div></div>
    <div class="comment" style="top:559px"><b>Anonym @ Your Story</b>Happy Birthday's Tavolin..<br>wish u all the best ;)</div>
    <div class="rule" style="left:904px;top:619px;width:162px"></div>
    <div class="comment-thumb" style="top:635px"><div class="pic pic-parchment" role="img" aria-label="Colourful road lines on aged paper"></div></div>
    <div class="comment" style="top:636px"><b>Anonym @ Your Story</b>Happy Birthday's Tavolin..<br>wish u all the best ;)</div>
    <div class="rule" style="left:904px;top:696px;width:162px"></div>
    <div class="comment-thumb" style="top:712px"><div class="pic pic-parchment" role="img" aria-label="Colourful road lines on aged paper"></div></div>
    <div class="comment" style="top:713px"><b>Anonym @ Your Story</b>Happy Birthday's Tavolin..<br>wish u all the best ;)</div>
    <div class="rule" style="left:904px;top:773px;width:162px"></div>
  </div>
</body>
</html>
```